Landing page for 'Page under construction' page

We need a simple landing page that we can use while our page is under construction.

The page should be made ready so that all we need to do is drop it on our web server and then it will function as our webpage. The domain is www.tlv.no

Please see attached file for instructions on what elements to include in the landing page. The Brand Book provides fonts and color palette.

Coding

Coded - Design and coding required

Number of Pages Required

1 page

Colors

Designer to choose colors to be used in the design.

```html
<!DOCTYPE html>
<html lang="en">
<head>
<meta charset="utf-8">
<title>TLV – Page is under construction</title>
<link href="https://fonts.googleapis.com/css2?family=Poppins:wght@400;500;600;700&display=swap" rel="stylesheet">
<style>
:root{
  --navy:#27358a;
  --ink:#2f3440;
  --muted:#8a8f9c;
  --teal:#2aa6c9;
  --band:#f2f3f7;
  --icon-bg:#e6e4f4;
  --icon:#6b5fc4;
  --footer:#eceef3;
  --white:#ffffff;
}
*{margin:0;padding:0;box-sizing:border-box}
html,body{width:1200px;height:2432px;overflow:hidden;background:var(--white)}
body{font-family:'Poppins',sans-serif;color:var(--ink);text-align:center}
.section{position:relative;width:1200px}
.brand{font-weight:700;font-size:30px;color:var(--navy);letter-spacing:-.5px}

.hero{height:560px}
.hero .brand{position:absolute;top:30px;left:0;right:0}
.hero-art{position:absolute;top:110px;left:390px;width:420px;height:290px;background:linear-gradient(180deg,#f6f7fa,#e9ecf2);border-radius:8px}
.hero h1{position:absolute;top:418px;left:0;right:0;font-size:34px;font-weight:600}
.hero p{position:absolute;top:468px;left:0;right:0;font-size:17px;color:var(--muted)}
.btn{position:absolute;top:514px;left:530px;width:140px;height:36px;border-radius:18px;background:var(--teal);color:var(--white);font-size:13px;line-height:36px;font-weight:500}

.vision{height:600px;background:var(--band)}
.section-title{font-size:34px;font-weight:500;padding-top:78px}
.lead{font-size:16px;line-height:26px;color:var(--muted);width:560px;margin:14px auto 0}
.pillars{display:flex;justify-content:center;gap:140px;margin-top:66px}
.pillar{width:200px}
.pillar .icon{width:60px;height:60px;border-radius:50%;background:var(--icon-bg);margin:0 auto 14px;display:flex;align-items:center;justify-content:center}
.pillar h3{font-size:20px;font-weight:600}
.pillar p{font-size:14px;line-height:21px;color:var(--navy);margin-top:8px}

.values{height:600px}
.values .section-title{padding-top:40px}
.values-row{position:absolute;top:180px;left:280px;display:flex;gap:40px}
.team-photo{width:400px;height:300px;background:linear-gradient(135deg,#b7a99a,#4f5563);}
.value-list{list-style:none;text-align:left;padding-top:20px}
.value-list li{font-size:30px;font-weight:700;color:var(--navy);line-height:58px;padding-left:30px;position:relative}
.value-list li::before{content:"";position:absolute;left:4px;top:25px;width:9px;height:9px;border-radius:50%;background:var(--navy)}
.know-more{font-size:22px;color:var(--ink);padding-left:30px;margin-top:-2px}

.focus{height:360px;background:var(--band)}
.focus .section-title{padding-top:90px;color:#5b606c;font-size:30px}
.focus p{width:620px;margin:18px auto 0;font-size:13px;line-height:19px;color:var(--muted)}

.contact{height:208px}
.contact .section-title{padding-top:68px;font-size:30px;color:#5b606c}
.contact p{font-size:13px;color:var(--muted);margin-top:10px}

.footer{height:104px;background:var(--footer);display:flex;align-items:center;justify-content:space-between;padding:0 180px}
.footer .brand{font-size:24px}
.footer small{font-size:13px;color:var(--muted)}
.footer nav{display:flex;gap:22px;font-size:13px;color:var(--muted)}
</style>
</head>
<body>
<header class="section hero">
  <div class="brand">Ledgerline</div>
  <div class="hero-art" role="img" aria-label="Line illustration of a workspace with rocket, laptop, phone and lamp"></div>
  <h1>Page is under construction</h1>
  <p>Digital solutions and data-driven business development that create value</p>
  <div class="btn">Have write us</div>
</header>

<section class="section vision">
  <h2 class="section-title">TLV Vision</h2>
  <p class="lead">TLV will be the country's leading supplier and competence house on Ledgerline software and digital solutions for business management</p>
  <div class="pillars">
    <div class="pillar">
      <div class="icon"><svg width="26" height="26" viewBox="0 0 26 26" fill="none" stroke="var(--icon)" stroke-width="2"><rect x="4" y="3" width="18" height="20" rx="2"/><path d="M8 9h10M8 13h10M8 17h6"/></svg></div>
      <h3>plan</h3>
      <p>Budgeting &amp; Forecasting</p>
    </div>
    <div class="pillar">
      <div class="icon"><svg width="26" height="26" viewBox="0 0 26 26" fill="none" stroke="var(--icon)" stroke-width="2"><circle cx="13" cy="13" r="9"/><path d="M9 13l3 3 5-6"/></svg></div>
      <h3>Execute</h3>
      <p>Consolidation<br>Loan portfolio manager<br>Custom reaction application</p>
    </div>
    <div class="pillar">
      <div class="icon"><svg width="26" height="26" viewBox="0 0 26 26" fill="none" stroke="var(--icon)" stroke-width="2"><circle cx="11" cy="11" r="7"/><path d="M16 16l6 6"/></svg></div>
      <h3>Analyze</h3>
      <p>Reporting and Dashboard<br>Simulate &amp; Prediction<br>Self service</p>
    </div>
  </div>
</section>

<section class="section values">
  <h2 class="section-title">TLV Vision</h2>
  <p class="lead">TLV will be the country's leading supplier and competence house on Ledgerline software and digital solutions for business management</p>
  <div class="values-row">
    <div class="team-photo" role="img" aria-label="Photo of the team standing together in the office"></div>
    <div>
      <ul class="value-list">
        <li>Passionate</li>
        <li>Accountability</li>
        <li>Innovative</li>
        <li>Value creation</li>
        <li>Competent</li>
      </ul>
      <div class="know-more">Know more</div>
    </div>
  </div>
</section>

<section class="section focus">
  <h2 class="section-title">Focus</h2>
  <p>At TLV we work purposefully to help clients reach their goals with modern planning and reporting. Our advisors combine deep business knowledge with solid technical skills, and guide every project from first workshop to live solution. We build budgets, forecasts and dashboards on one shared platform, so finance teams spend less time on spreadsheets and more on analysis. Together with our clients we create structured processes, reliable numbers and better decisions, and we keep improving the solution as the business grows and changes over time.</p>
</section>

<section class="section contact">
  <h2 class="section-title">Contact</h2>
  <p>Tlf: +47 22 00 00 00 &nbsp;·&nbsp; Contact us: post@tlv.no</p>
</section>

<footer class="section footer">
  <div class="brand">Ledgerline</div>
  <small>© Ledgerline 2020 Rights Reserved</small>
  <nav><span>Follow</span><span>News</span><span>Network</span></nav>
</footer>
</body>
</html>
```